Casas de Nueva Aurora Flyer

Make me a flyer postcard 5 x 7 horizontal, one sided. I want main title to be "Casas de Nueva Aurora". It needs to say “Familias que se forman en la fe y valores humanos, y trabajan para llevar a otras familias al encuentro con Cristo y la Virgen María.”  We are in 4 places, include this:
Reuniones Cada Domingo
Los Olmos, Falls Church: 11:15am - 301-555-0142
Monte Claro, Sterling: 9:30am - 571-555-0187
Hogar Valle Sereno, 9:45am - 703-555-0163
Puerta Dorada, Winchester: 2:30pm - 540-555-0129
Include the logo attached, and use the picture attached as the main image, you can select the people from the image only and delete background or keep background but make it fit in nicely to the postcard.

```html
<!DOCTYPE html>
<html lang="es">
<head>
<meta charset="utf-8">
<title>Casas de Nueva Aurora</title>
<link rel="stylesheet" href="https://fonts.googleapis.com/css2?family=DM+Serif+Display&family=Gelasio:wght@600;700&display=swap">
<style>
  :root {
    --parchment-light: #f7e0ad;
    --parchment: #eec98a;
    --parchment-dark: #d9a863;
    --ink: #1e120b;
    --title-dark: #6b1606;
    --title-light: #c8500f;
    --panel-top: #661607;
    --panel-mid: #8a2a09;
    --panel-bottom: #d9600f;
    --cream: #fff3dc;
    --gold-light: #ffd24a;
    --gold-dark: #f5a417;
    --rule: #f0cf9a;
  }
  * { margin: 0; padding: 0; box-sizing: border-box; }
  html, body { width: 1200px; height: 930px; overflow: hidden; background: #d4d4d4; }
  .flyer {
    position: relative;
    width: 1200px; height: 930px; overflow: hidden;
    background:
      radial-gradient(ellipse at 50% 30%, var(--parchment-light) 0%, var(--parchment) 55%, var(--parchment-dark) 100%);
    font-family: "Gelasio", Georgia, serif;
    color: var(--ink);
  }
  .icon-frame {
    position: absolute; left: 157px; top: 42px; width: 142px; height: 215px;
    background: linear-gradient(160deg, #8a6a3a, #5a4323);
    clip-path: polygon(50% 0, 100% 14%, 100% 100%, 0 100%, 0 14%);
    padding: 12px;
  }
  .icon-art {
    width: 100%; height: 100%;
    background: linear-gradient(160deg, #c9963a 0%, #b3261c 45%, #7a1a14 100%);
    clip-path: polygon(50% 0, 100% 12%, 100% 100%, 0 100%, 0 12%);
  }
  .title {
    position: absolute; left: 352px; top: 30px;
    font-family: "DM Serif Display", Georgia, serif;
    font-size: 118px; line-height: 108px; letter-spacing: -1px;
    background: linear-gradient(180deg, var(--title-dark) 20%, var(--title-light) 100%);
    -webkit-background-clip: text; background-clip: text; color: transparent;
  }
  .title span { display: block; }
  .tagline {
    position: absolute; left: 0; right: 0; top: 282px;
    text-align: center; font-weight: 700; font-size: 23px; line-height: 32px;
  }
  .schedule {
    position: absolute; left: 53px; top: 362px; width: 1095px; bottom: 0;
    border-radius: 18px 18px 0 0;
    background: linear-gradient(180deg, var(--panel-top) 0%, var(--panel-top) 35%, var(--panel-mid) 62%, var(--panel-bottom) 100%);
    color: var(--cream);
  }
  .schedule-heading {
    position: absolute; left: 0; right: 0; top: 26px;
    text-align: center; font-weight: 700; font-size: 34px;
  }
  .rule { position: absolute; top: 43px; width: 190px; height: 10px; }
  .rule-left { left: 84px; }
  .rule-right { left: 798px; }
  .location { position: absolute; top: 111px; }
  .location h3 { font-weight: 700; font-size: 25px; line-height: 27px; height: 56px; }
  .time {
    margin-top: 10px; width: 141px; height: 34px;
    background: linear-gradient(180deg, var(--gold-light), var(--gold-dark));
    color: var(--ink); font-weight: 600; font-size: 24px; line-height: 34px; text-align: center;
  }
  .phone { margin-top: 8px; display: flex; align-items: center; gap: 5px; font-size: 22px; }
  .phone svg { width: 19px; height: 19px; flex: none; }
  .divider { position: absolute; top: 104px; width: 1px; height: 128px; background: var(--rule); opacity: .7; }
  .group-photo {
    position: absolute; left: 58px; top: 250px; width: 964px; bottom: 0;
    background: linear-gradient(180deg, rgba(120,40,10,0) 0%, rgba(150,70,30,.75) 30%, rgba(170,110,80,.9) 70%, rgba(200,110,50,.9) 100%);
    border-radius: 120px 120px 0 0;
  }
</style>
</head>
<body>
<div class="flyer">
  <div class="icon-frame"><div class="icon-art" role="img" aria-label="Icono enmarcado de la Sagrada Familia"></div></div>

  <h1 class="title"><span>Casas de</span><span>Nueva Aurora</span></h1>

  <p class="tagline">Familias que se forman en la fe y valores humanos, y trabajan para llevar a<br>otras familias al encuentro con Cristo y la Virgen María</p>

  <section class="schedule">
    <svg class="rule rule-left" viewBox="0 0 190 10"><line x1="5" y1="5" x2="185" y2="5" stroke="#f0cf9a" stroke-width="2"/><circle cx="5" cy="5" r="4" fill="#f0cf9a"/><circle cx="185" cy="5" r="4" fill="#f0cf9a"/></svg>
    <h2 class="schedule-heading">Reuniones Cada Domingo</h2>
    <svg class="rule rule-right" viewBox="0 0 190 10"><line x1="5" y1="5" x2="185" y2="5" stroke="#f0cf9a" stroke-width="2"/><circle cx="5" cy="5" r="4" fill="#f0cf9a"/><circle cx="185" cy="5" r="4" fill="#f0cf9a"/></svg>

    <div class="location" style="left:52px">
      <h3>Los Olmos,<br>Falls Church</h3>
      <div class="time">11:15am</div>
      <div class="phone"><svg viewBox="0 0 20 20"><circle cx="10" cy="10" r="10" fill="#f5a417"/><path d="M7 5.5l1.6 2.4-1 1.1a6 6 0 0 0 3.4 3.4l1.1-1 2.4 1.6-.8 1.6c-4 .2-8-3.8-7.8-7.8z" fill="#661607"/></svg>301-555-0142</div>
    </div>
    <div class="divider" style="left:245px"></div>

    <div class="location" style="left:293px">
      <h3>Monte Claro,<br>Sterling</h3>
      <div class="time">9:30am</div>
      <div class="phone"><svg viewBox="0 0 20 20"><circle cx="10" cy="10" r="10" fill="#f5a417"/><path d="M7 5.5l1.6 2.4-1 1.1a6 6 0 0 0 3.4 3.4l1.1-1 2.4 1.6-.8 1.6c-4 .2-8-3.8-7.8-7.8z" fill="#661607"/></svg>571-555-0187</div>
    </div>
    <div class="divider" style="left:506px"></div>

    <div class="location" style="left:565px">
      <h3>Hogar<br>Valle Sereno</h3>
      <div class="time">9:45am</div>
      <div class="phone"><svg viewBox="0 0 20 20"><circle cx="10" cy="10" r="10" fill="#f5a417"/><path d="M7 5.5l1.6 2.4-1 1.1a6 6 0 0 0 3.4 3.4l1.1-1 2.4 1.6-.8 1.6c-4 .2-8-3.8-7.8-7.8z" fill="#661607"/></svg>703-555-0163</div>
    </div>
    <div class="divider" style="left:780px"></div>

    <div class="location" style="left:823px">
      <h3>Puerta Dorada,<br>Winchester</h3>
      <div class="time">2:30pm</div>
      <div class="phone"><svg viewBox="0 0 20 20"><circle cx="10" cy="10" r="10" fill="#f5a417"/><path d="M7 5.5l1.6 2.4-1 1.1a6 6 0 0 0 3.4 3.4l1.1-1 2.4 1.6-.8 1.6c-4 .2-8-3.8-7.8-7.8z" fill="#661607"/></svg>540-555-0129</div>
    </div>

    <div class="group-photo" role="img" aria-label="Foto grupal de las familias de la comunidad reunidas al aire libre"></div>
  </section>
</div>
</body>
</html>
```